Lanterns over lake/list. Wedding planning checklist design

We are a wedding videography start-up that's about to launch a chatterleaf campaign. We need a simple yet premium looking design to showcase a wedding planning checklist which we have written. The main focus of the design should be:

- On A4 pages
- Appeal to young engaged women
- Anyone at home can print it off and stick it onto a fridge
- Premium looking

The contents doesn't have to be on one piece of A4, the list can span more than one page. Also, it doesn't have to be traditional folded brochure style, a full A4 sized list is preferred. The design will potentially be used in further A4 brochure style blog posts. The written checklist and our company logo is attached for reference.

Target Market(s)

Young engaged woman

Industry/Entity Type

Wedding

Requirements
Must have
• Simple and premium feel.
Nice to have
• flexible design that can be reused in the future for blog posts.

```html
<!DOCTYPE html>
<html lang="en">
<head>
<meta charset="utf-8">
<title>Lanterns over lake/list – Wedding Planning Checklist</title>
<link rel="stylesheet" href="https://fonts.googleapis.com/css2?family=Didact+Gothic&family=Poppins:wght@600&display=swap">
<style>
  :root {
    --ink: #3b3036;
    --rose: #d985b4;
    --rose-deep: #c4669b;
    --blush: #efb3d2;
    --glow: #f7e6a8;
    --rule: rgba(196, 102, 155, 0.55);
    --figure-dark: #4a3a34;
    --figure-light: #f6f0dc;
    --petal: #f2a9b9;
  }
  * { margin: 0; padding: 0; box-sizing: border-box; }
  html, body { width: 848px; height: 1200px; overflow: hidden; }
  body { font-family: "Didact Gothic", sans-serif; color: var(--ink); }
  .checklist { position: relative; width: 848px; height: 1200px; overflow: hidden; }
  .backdrop {
    position: absolute; inset: 0;
    background:
      radial-gradient(ellipse 210px 420px at 440px 700px, rgba(247,230,168,0.85), rgba(247,230,168,0) 100%),
      radial-gradient(ellipse 180px 300px at 560px 780px, rgba(214,130,170,0.6), rgba(214,130,170,0) 100%),
      linear-gradient(180deg, var(--rose) 0%, var(--blush) 45%, #f3c6d8 100%);
  }
  .illustration { position: absolute; border-radius: 40% 40% 8px 8px; opacity: 0.9; }
  .couple {
    background: linear-gradient(90deg, var(--figure-dark) 0%, var(--figure-dark) 42%, var(--figure-light) 42%, var(--figure-light) 100%);
  }
  .flowers {
    position: absolute; left: 616px; top: 700px; width: 205px; height: 62px;
    border-radius: 30px;
    background: linear-gradient(90deg, var(--petal), #8fbf86 30%, var(--petal) 55%, #8fbf86 80%, var(--petal));
    opacity: 0.85;
  }
  .stage-heading {
    position: absolute; left: 163px;
    font-family: "Poppins", sans-serif; font-weight: 600;
    font-size: 27px; line-height: 1; letter-spacing: 0.3px;
    padding-bottom: 4px; border-bottom: 1px dashed var(--rule);
  }
  .row {
    position: absolute; left: 160px; width: 620px;
    display: flex; font-size: 13.2px; line-height: 15.2px; letter-spacing: 0.4px;
    padding-bottom: 6px; border-bottom: 1px dashed var(--rule);
  }
  .task { width: 314px; padding-left: 12px; text-indent: -10px; font-size: 14px; line-height: 16.5px; }
  .task::before { content: "•"; display: inline-block; width: 10px; text-indent: 0; }
  .note { width: 306px; }
</style>
</head>
<body>
<main class="checklist">
  <div class="backdrop" role="img" aria-label="Soft pink photo of a bride and groom walking arm in arm down a path"></div>

  <div class="illustration couple" style="left:18px;top:146px;width:139px;height:144px" role="img" aria-label="Illustration of a groom embracing a bride"></div>
  <div class="illustration couple" style="left:13px;top:544px;width:141px;height:138px" role="img" aria-label="Illustration of a bride and groom holding hands"></div>
  <div class="illustration couple" style="left:10px;top:959px;width:144px;height:123px" role="img" aria-label="Illustration of a groom kneeling to propose to a bride"></div>
  <div class="flowers" role="img" aria-label="Watercolour pink roses with green leaves"></div>

  <h2 class="stage-heading" style="top:44px">12 months</h2>
  <div class="row" style="top:82px"><p class="task">Decide on a date and venue</p><p class="note">The earlier you can reserve these, the better! Will it be a church, garden or beach wedding?</p></div>
  <div class="row" style="top:123px"><p class="task">Organise a meeting of the parents and determine your budget</p><p class="note">Work out how much each family is contributing so that there are no surprises</p></div>
  <div class="row" style="top:167px"><p class="task">Choose the type of wedding</p><p class="note">Form a basic idea of the kind of wedding you would like to have e.g.- simple or lavish?</p></div>
  <div class="row" style="top:210px"><p class="task">Pick your wedding party</p><p class="note">Best man, groomsmen, maid of honor, bridesmaids, flower girl, ring bearer etc.</p></div>
  <div class="row" style="top:251px"><p class="task">Pick or hire a MC</p><p class="note">Someone who enjoys being in the limelight, is confident telling a few jokes, and will make sure everyone is having a good time</p></div>
  <div class="row" style="top:304px"><p class="task">Start a wedding folder</p><p class="note">This is where you can compile your notes and ideas about anything wedding related</p></div>
  <div class="row" style="top:345px"><p class="task">Hire a planner</p><p class="note">A planner will take the stress off you and they can negotiate good deals with vendors</p></div>
  <div class="row" style="top:386px"><p class="task">Start your guest list</p><p class="note">Be realistic about the number of guests to avoid stress later on</p></div>
  <div class="row" style="top:425px"><p class="task">Research your wedding professionals (vendors?)</p><p class="note">These include your videographers, photographers, caterer, DJ, florist, decorator etc. Wedding planners can help with this!</p></div>
  <div class="row" style="top:477px"><p class="task">Start shopping for wedding rings and your dress</p><p class="note">The sooner you buy them, the sooner you can check it off your list</p></div>

  <h2 class="stage-heading" style="top:536px">9 months</h2>
  <div class="row" style="top:577px"><p class="task">Book your official videographers</p><p class="note">Lanterns &amp; Co are the way to go! (LOL)</p></div>
  <div class="row" style="top:603px"><p class="task">Book your photographer</p><p class="note">Consider having an unplugged wedding</p></div>
  <div class="row" style="top:627px"><p class="task">Book your DJ, florist, caterer, decorator and wedding cake</p><p class="note">Use your friends circle! (Friends as vendors) This can be a big cost-cutter</p></div>
  <div class="row" style="top:666px"><p class="task">Book your celebrant</p><p class="note">Have some good conversations with them to determine if they're the right fit</p></div>

  <h2 class="stage-heading" style="top:734px">6 months</h2>
  <div class="row" style="top:774px"><p class="task">Buy wedding party suits/dresses</p><p class="note">Your bridal party should complement your gown/suit, but be sure to consider figure types and coloring when selecting outfits</p></div>
  <div class="row" style="top:826px"><p class="task">Book wedding car</p><p class="note">Try and book this as soon as you can to ensure you get the car of your dreams</p></div>
  <div class="row" style="top:863px"><p class="task">Get your engagement photos done</p><p class="note">These can be used for your save-the-date cards. It's also the perfect time to test out your photographer before the big day</p></div>
  <div class="row" style="top:917px"><p class="task">Launch a website</p><p class="note">A good way to broadcast your registry details loud and clear</p></div>
  <div class="row" style="top:961px"><p class="task">Finalise guest list</p><p class="note">Try to avoid any last-minute add-ons. Don't let your parents or in-laws bully you!</p></div>

  <h2 class="stage-heading" style="top:1026px">5 months</h2>
  <div class="row" style="top:1063px"><p class="task">Purchase dress and any other accessories and shoes</p><p class="note">These can include veils, hair pieces, jewellery. But remember: less is more</p></div>
  <div class="row" style="top:1103px"><p class="task">Send out the save-the-date notices</p><p class="note">Send these as cards, chatterleaf notice or even as a video</p></div>
</main>
</body>
</html>
```